ZESTMUNCHY
Zestmunchy is a food van, serving high vibe delicious food to go. This business is dedicated to healthy delicious feel good food, beauty in service and a sustainable planet.

The van will operate in the south west of western Australia at music festivals events markets wherever people need great food to go!

I like the idea of vibrant green mixed with a yellow?? background with some rays like the sun through the background.
The font needs to say vibrant energetic
TO ME -vibrant energetic font has to appear to be on the move - perhaps with shading??

I like fusha if that works for font? but the colour has to say food too.

I would like a symbol on the card a simple V turned into a womans raised arms. This should be vibrant too.
Thank you
Blessings
Marisol

Target Market(s)

target lovers of healthy high vibe food. music festival goers. age 18- 50 feel. audiance conscious eaters of feel great food

Industry/Entity Type

Events

Contact Information for Business Card

ZESTMUNCHY
High Vibe Food
Van
Marisol -owner/opperator
0458170396
Face book symbol - ZESTMUNCHY

on the I would like a logo of a simple V turned into a womans arms up toward the sky flip side

My number and name again
Zestmunchy- feel great mobile food
Festivals, events, markets & where high vibe food 2 go is appreciated

Requirements
Nice to have
• Moving energetic font
colour that says high vibe and healthy food

a logo that is a simple V turned into a woman's raised arms in gratitude

```html
<!DOCTYPE html>
<html lang="en">
<head>
<meta charset="utf-8">
<title>Zestmunchy business card</title>
<link href="https://fonts.googleapis.com/css2?family=Open+Sans:wght@400;600;700;800&display=swap" rel="stylesheet">
<style>
  :root {
    --bg: #e4e4e4;
    --green-dark: #22a84a;
    --green-light: #7cc242;
    --green-line: #5cb83c;
    --brand: #9bcf3a;
    --ink: #1f1f1f;
    --panel-grey: #d2d2d2;
    --panel-light: #f2f2f2;
    --text-dark: #2a2a2a;
    --rule: #c4c4c4;
  }
  * { box-sizing: border-box; margin: 0; padding: 0; }
  html, body { width: 1200px; height: 1173px; overflow: hidden; }
  body {
    background: var(--bg);
    font-family: "Open Sans", Arial, sans-serif;
    position: relative;
  }
  .card {
    position: absolute;
    top: 186px;
    width: 460px;
    height: 800px;
    padding: 30px;
    background: linear-gradient(160deg, var(--green-dark) 0%, var(--green-light) 100%);
    box-shadow: 0 6px 14px rgba(0,0,0,0.18);
  }
  .card--back { left: 90px; }
  .card--front { left: 650px; }

  .card__inner {
    width: 100%;
    height: 100%;
    overflow: hidden;
    display: flex;
    flex-direction: column;
  }
  .card--back .card__inner { border-radius: 0 60px 0 60px; background: var(--ink); }
  .card--front .card__inner { border-radius: 60px 0 60px 0; background: var(--panel-light); }

  .back__web {
    height: 130px;
    background: var(--panel-grey);
    border-bottom: 10px solid var(--green-line);
    display: flex;
    align-items: center;
    justify-content: center;
    font-size: 22px;
    color: var(--text-dark);
    letter-spacing: 0.5px;
  }
  .back__brand {
    flex: 1;
    display: flex;
    align-items: center;
    justify-content: center;
    gap: 12px;
  }
  .brand {
    display: flex;
    align-items: center;
    gap: 10px;
  }
  .brand-mark {
    border-radius: 50%;
    background: var(--brand);
    flex-shrink: 0;
  }
  .brand-name {
    font-weight: 800;
    color: var(--brand);
    font-family: "Open Sans", Arial, sans-serif;
    line-height: 1;
  }
  .back__brand .brand-mark { width: 40px; height: 40px; }
  .back__brand .brand-name { font-size: 50px; }

  .front__head {
    height: 150px;
    background: var(--ink);
    display: flex;
    align-items: center;
    justify-content: center;
  }
  .front__head .brand-mark { width: 32px; height: 32px; }
  .front__head .brand-name { font-size: 40px; }

  .contact-list {
    list-style: none;
    flex: 1;
    padding: 30px 30px 0 34px;
  }
  .contact-item {
    display: flex;
    align-items: center;
    gap: 24px;
    height: 94px;
  }
  .contact-icon {
    width: 44px; height: 44px;
    border: 3px solid var(--green-line);
    border-radius: 50%;
    display: flex; align-items: center; justify-content: center;
    flex-shrink: 0;
  }
  .contact-icon svg { width: 22px; height: 22px; }
  .contact-text {
    flex: 1;
    align-self: stretch;
    display: flex;
    align-items: center;
    font-size: 19px;
    color: var(--text-dark);
    line-height: 1.3;
    border-bottom: 2px solid var(--rule);
  }
  .contact-item:last-child .contact-text { border-bottom: none; }

  .front__person {
    height: 180px;
    background: var(--panel-grey);
    display: flex;
    flex-direction: column;
    justify-content: center;
    padding-left: 102px;
  }
  .person-name {
    font-size: 31px;
    font-weight: 700;
    color: var(--text-dark);
    letter-spacing: 1px;
  }
  .person-role {
    font-size: 27px;
    color: var(--text-dark);
  }
</style>
</head>
<body>

  <section class="card card--back">
    <div class="card__inner">
      <div class="back__web">www.zestmunchyvan.com</div>
      <div class="back__brand">
        <span class="brand">
          <span class="brand-mark" role="img" aria-label="Zestmunchy symbol"></span>
          <span class="brand-name">Zestmunchy</span>
        </span>
      </div>
    </div>
  </section>

  <section class="card card--front">
    <div class="card__inner">
      <header class="front__head">
        <span class="brand">
          <span class="brand-mark" role="img" aria-label="Zestmunchy symbol"></span>
          <span class="brand-name">Zestmunchy</span>
        </span>
      </header>

      <ul class="contact-list">
        <li class="contact-item">
          <span class="contact-icon">
            <svg viewBox="0 0 24 24" fill="#5cb83c"><path d="M6.6 10.8a15.1 15.1 0 0 0 6.6 6.6l2.2-2.2a1 1 0 0 1 1-.25 11.4 11.4 0 0 0 3.6.57 1 1 0 0 1 1 1V20a1 1 0 0 1-1 1A17 17 0 0 1 3 4a1 1 0 0 1 1-1h3.5a1 1 0 0 1 1 1c0 1.25.2 2.45.57 3.57a1 1 0 0 1-.25 1z"/></svg>
          </span>
          <span class="contact-text">0458170396</span>
        </li>
        <li class="contact-item">
          <span class="contact-icon">
            <svg viewBox="0 0 24 24" fill="none" stroke="#5cb83c" stroke-width="2.2"><rect x="3" y="6" width="18" height="12"/><path d="M3 6l9 7 9-7"/></svg>
          </span>
          <span class="contact-text">hello@zestmunchy.com</span>
        </li>
        <li class="contact-item">
          <span class="contact-icon">
            <svg viewBox="0 0 24 24" fill="none" stroke="#5cb83c" stroke-width="1.8"><circle cx="12" cy="12" r="9"/><ellipse cx="12" cy="12" rx="4" ry="9"/><path d="M3 12h18M5 7h14M5 17h14"/></svg>
          </span>
          <span class="contact-text">www.zestmunchyvan.com</span>
        </li>
        <li class="contact-item">
          <span class="contact-icon">
            <svg viewBox="0 0 24 24" fill="#5cb83c"><path d="M12 2a7 7 0 0 0-7 7c0 5 7 13 7 13s7-8 7-13a7 7 0 0 0-7-7zm0 9.5A2.5 2.5 0 1 1 12 6.5a2.5 2.5 0 0 1 0 5z"/></svg>
          </span>
          <span class="contact-text">Unit 450,GH, UK, T4P 3K8<br>212 Fern Street NW</span>
        </li>
      </ul>

      <footer class="front__person">
        <span class="person-name">MARISOL</span>
        <span class="person-role">Founder</span>
      </footer>
    </div>
  </section>

</body>
</html>
```